Granite, Zinc and Clay Roofing LLC needs a new business card

I need a new business card because I have a new address.
I do slate copper and tile roofs. My webpage is: www.granitezincandclayroofing.example

```html
<!DOCTYPE html>
<html lang="en">
<head>
<meta charset="utf-8">
<title>Granite, Zinc and Clay Roofing – Business Card</title>
<link rel="stylesheet" href="https://fonts.googleapis.com/css2?family=Arimo:wght@400;700&display=swap">
<style>
  :root {
    --page-bg: #c9cbcd;
    --card-black: #000000;
    --sky-blue: #59b6e7;
    --sky-blue-light: #6cc0ea;
    --sky-blue-deep: #4faee3;
    --silver: #c8cacc;
    --silver-dark: #8d9093;
    --white: #ffffff;
  }
  * { box-sizing: border-box; margin: 0; padding: 0; }
  html, body {
    width: 1187px; height: 1200px; overflow: hidden;
    background: var(--page-bg);
    font-family: "Arimo", Arial, sans-serif;
  }
  .canvas { position: relative; width: 1187px; height: 1200px; }

  .card { position: absolute; width: 772px; height: 439px; overflow: hidden; }
  .card-front { left: 207px; top: 117px; background: var(--card-black); }
  .card-back { left: 209px; top: 641px; background: var(--card-black); }

  /* front */
  .front-mark {
    position: absolute; left: 0; right: 0; top: 0; height: 362px;
    display: flex; align-items: center; justify-content: center; gap: 18px;
  }
  .mark-square { width: 26px; height: 26px; background: var(--white); flex: none; }
  .mark-name {
    color: var(--white); font-weight: 400; font-size: 40px; line-height: 1.15;
  }
  .front-rule {
    position: absolute; left: 0; right: 0; top: 362px; height: 6px;
    background: linear-gradient(90deg, var(--silver-dark), var(--silver), var(--white), var(--silver), var(--silver-dark));
  }
  .front-band {
    position: absolute; left: 0; right: 0; top: 368px; bottom: 0;
    background: linear-gradient(90deg, var(--sky-blue-light), var(--sky-blue-deep));
    display: flex; align-items: center; justify-content: center;
  }
  .front-web { color: var(--white); font-weight: 700; font-size: 21px; letter-spacing: 1px; }

  /* back */
  .back-brand {
    position: absolute; left: 0; top: 0; width: 399px; height: 100%;
    background: linear-gradient(180deg, var(--sky-blue-light), var(--sky-blue-deep));
    display: flex; align-items: center; justify-content: center; gap: 12px;
  }
  .back-brand .mark-square { background: var(--card-black); width: 20px; height: 20px; }
  .back-brand .mark-name { color: var(--card-black); font-size: 28px; }
  .back-divider {
    position: absolute; left: 399px; top: 0; width: 5px; height: 100%;
    background: linear-gradient(180deg, var(--silver), var(--white), var(--silver-dark));
  }
  .contact { position: absolute; left: 437px; top: 86px; right: 14px; color: var(--white); }
  .contact-name { font-size: 33px; line-height: 1; font-weight: 400; white-space: nowrap; }
  .contact-role { font-size: 27px; line-height: 1.2; margin-left: 2px; }
  .contact-address { font-size: 22px; line-height: 33px; margin-top: 30px; }
  .contact-lines { list-style: none; margin-top: 18px; font-size: 22px; line-height: 29px; }
  .contact-lines li { display: flex; align-items: flex-start; gap: 7px; }
  .contact-lines svg { width: 15px; height: 15px; flex: none; margin-top: 7px; }
  .contact-web { word-break: normal; overflow-wrap: normal; }
  .icon-fill { fill: var(--sky-blue); }
  .icon-line { fill: none; stroke: var(--sky-blue); }
</style>
</head>
<body>
<main class="canvas">
  <section class="card card-front" aria-label="Business card front">
    <div class="front-mark">
      <span class="mark-square"></span>
      <p class="mark-name">Granite, Zinc and Clay<br>Roofing</p>
    </div>
    <div class="front-rule"></div>
    <div class="front-band"><p class="front-web">www.granitezincandclayroofing.example</p></div>
  </section>

  <section class="card card-back" aria-label="Business card back">
    <div class="back-brand">
      <span class="mark-square"></span>
      <p class="mark-name">Granite, Zinc and Clay<br>Roofing</p>
    </div>
    <div class="back-divider"></div>
    <div class="contact">
      <h1 class="contact-name">Andras (Andy) Toth</h1>
      <p class="contact-role">Owner</p>
      <p class="contact-address">27810 Millbrook Rd.<br>Millbrook, OH 44999</p>
      <ul class="contact-lines">
        <li>
          <svg viewBox="0 0 16 16" aria-hidden="true"><path class="icon-fill" d="M3 1l3 0 1 4-2 1.5c1 2 2.5 3.5 4.5 4.5L11 9l4 1v3c0 1-1 2-2 2C7 15 1 9 1 3c0-1 1-2 2-2z"/></svg>
          <span>(555)014-2730</span>
        </li>
        <li>
          <svg viewBox="0 0 16 16" aria-hidden="true"><g class="icon-line" stroke-width="1.4"><circle cx="8" cy="8" r="6.5"/><ellipse cx="8" cy="8" rx="2.8" ry="6.5"/><path d="M1.5 8h13M2.5 4.8h11M2.5 11.2h11"/></g></svg>
          <span class="contact-web">www.granitezincandclayroofing<wbr>.example</span>
        </li>
        <li>
          <svg viewBox="0 0 16 16" aria-hidden="true"><rect class="icon-fill" x="1" y="3" width="14" height="10"/><path d="M1 3l7 6 7-6" fill="none" stroke="#000" stroke-width="1.3"/></svg>
          <span>gzcroofingllc@example.com</span>
        </li>
      </ul>
    </div>
  </section>
</main>
</body>
</html>
```